Dorsey Construction Law P.A.

Business Card with Corporate Logo. For a law firm specializing in construction law.

need address, telephone, email and website. Also, have an elegant and conservative logo.

Logo so it is DCL.

Full name "Gordon T. Dorsey

Under my name title "Attorney at Law"

Under title "Board Certified in Construction Law"

PA in email is lower case

Add logo to back side of card

Mix in a bit of gold color into card to go with the green

Some color on bottom
Updates

Target Market(s)

legal

Industry/Entity Type

Construction

Contact Information for Business Card

I like it -- edits: 1. add "L" to logo so it is DCL. 2. add my full name "Gordon T. Business Card with Corporate Logo. For a law firm specializing in construction law.

Logo so it is DCL.

PA in email is lower case

Font styles to use
Serif

Colors
00a990
f78f20

Requirements
Must have
• Conservative legal designed logo for construction market
• Address:
• Dorsey Construction Law, P.A.
• 4150 Harbor Pine Rd East, Ste B5
• Jacksonville, Florida 32217
• Main: 904-555-3817
• Direct: 904-555-4932
• Fax: 904-555-4932
• gt@dorseypa.example
• www.dorseyconstructionlaw.example
Nice to have
• Catchy conservative logo on card
Should not have
• Flashy

```html
<!DOCTYPE html>
<html lang="en">
<head>
<meta charset="utf-8">
<title>Dorsey Construction Law, P.A. — Business Card</title>
<link rel="stylesheet" href="https://fonts.googleapis.com/css2?family=Cinzel:wght@400&family=Crimson+Text:wght@400&display=swap">
<style>
  :root {
    --backdrop: #e6e6e6;
    --card: #ffffff;
    --teal: #0e7f83;
    --gold: #c6a466;
    --ink: #3a3a3a;
    --card-w: 520px;
    --card-h: 297px;
  }
  * { box-sizing: border-box; margin: 0; padding: 0; }
  html, body { width: 1200px; height: 675px; overflow: hidden; }
  body {
    background: var(--backdrop);
    font-family: "Crimson Text", Georgia, serif;
    color: var(--ink);
    position: relative;
  }
  .card {
    position: absolute;
    top: 189px;
    width: var(--card-w);
    height: var(--card-h);
    background: var(--card);
    box-shadow: 0 4px 14px rgba(0,0,0,0.12);
    overflow: hidden;
  }
  .card--front { left: 54px; }
  .card--back { left: 626px; }

  .band {
    position: absolute;
    left: 0; right: 0;
    bottom: 0;
    height: 12px;
    display: flex;
  }
  .band__teal { background: var(--teal); }
  .band__gold { background: var(--gold); }
  .card--front .band__teal { flex: 0 0 70%; }
  .card--front .band__gold { flex: 1; }
  .card--back .band__teal { flex: 0 0 64%; }
  .card--back .band__gold { flex: 1; }

  .firm {
    position: absolute;
    display: flex;
    align-items: center;
  }
  .firm__dot {
    border-radius: 50%;
    background: var(--teal);
    flex: none;
  }
  .firm__name {
    font-family: "Cinzel", "Times New Roman", serif;
    font-weight: 400;
    color: var(--teal);
    line-height: 1.02;
  }
  .card--front .firm { left: 56px; top: 78px; gap: 26px; }
  .card--front .firm__dot { width: 112px; height: 112px; }
  .card--front .firm__name { font-size: 30px; letter-spacing: 0.5px; }

  .card--back .firm { left: 30px; top: 32px; gap: 14px; }
  .card--back .firm__dot { width: 70px; height: 70px; }
  .card--back .firm__name { font-size: 19px; }

  .person {
    position: absolute;
    right: 30px;
    top: 34px;
    text-align: right;
  }
  .person__name {
    font-family: "Cinzel", "Times New Roman", serif;
    color: var(--teal);
    font-size: 20px;
    line-height: 1.1;
  }
  .person__title { font-size: 13px; line-height: 1.25; }

  .details {
    position: absolute;
    list-style: none;
    font-size: 13px;
    line-height: 1.3;
  }
  .details li { display: flex; align-items: flex-start; gap: 9px; margin-bottom: 4px; }
  .details svg { flex: none; width: 12px; height: 12px; margin-top: 2px; fill: var(--teal); }
  .details--location { right: 30px; top: 150px; }
  .details--contact { left: 30px; bottom: 34px; }
  .web { color: var(--teal); }
</style>
</head>
<body>

<section class="card card--front" aria-label="Card front">
  <div class="firm">
    <span class="firm__dot"></span>
    <p class="firm__name">Dorsey<br>Construction<br>Law, P.A.</p>
  </div>
  <div class="band"><span class="band__teal"></span><span class="band__gold"></span></div>
</section>

<section class="card card--back" aria-label="Card back">
  <div class="firm">
    <span class="firm__dot"></span>
    <p class="firm__name">Dorsey<br>Construction<br>Law, P.A.</p>
  </div>

  <div class="person">
    <p class="person__name">Gordon T. Dorsey</p>
    <p class="person__title">Attorney at Law</p>
    <p class="person__title">Board Certified in Construction Law</p>
  </div>

  <ul class="details details--location">
    <li>
      <svg viewBox="0 0 12 12" aria-hidden="true"><path d="M6 0a4 4 0 0 0-4 4c0 3 4 8 4 8s4-5 4-8a4 4 0 0 0-4-4zm0 5.6A1.6 1.6 0 1 1 6 2.4a1.6 1.6 0 0 1 0 3.2z"/></svg>
      <span>4150 Harbor Pine Rd East, Ste B5<br>Jacksonville, FL 32217</span>
    </li>
    <li>
      <svg viewBox="0 0 12 12" aria-hidden="true"><circle cx="6" cy="6" r="5.2" fill="none" stroke="#0e7f83" stroke-width="1.3"/><path d="M1 6h10M6 1c-2.6 3-2.6 7 0 10M6 1c2.6 3 2.6 7 0 10" fill="none" stroke="#0e7f83" stroke-width="1"/></svg>
      <span>www.<span class="web">dorseyconstructionlaw</span>.example</span>
    </li>
  </ul>

  <ul class="details details--contact">
    <li>
      <svg viewBox="0 0 12 12" aria-hidden="true"><path d="M1 4c0-2 2-3 5-3s5 1 5 3l-2.5.6L8 3H4l-.5 1.6zM3 6l1-2h4l1 2v5H3z"/></svg>
      <span>904-555-3817</span>
    </li>
    <li>
      <svg viewBox="0 0 12 12" aria-hidden="true"><path d="M1 4c0-2 2-3 5-3s5 1 5 3l-2.5.6L8 3H4l-.5 1.6zM3 6l1-2h4l1 2v5H3z"/></svg>
      <span>904-555-4932</span>
    </li>
    <li>
      <svg viewBox="0 0 12 12" aria-hidden="true"><path d="M0 2h12v8H0z"/><path d="M0.5 2.5 6 7l5.5-4.5" fill="none" stroke="#fff" stroke-width="1.1"/></svg>
      <span>gt@dorseypa.example</span>
    </li>
  </ul>

  <div class="band"><span class="band__teal"></span><span class="band__gold"></span></div>
</section>

</body>
</html>
```